New Business Card Design Project

Make a kick ass business card for The Otter Tea Mug, using the designs. I also might like the 2nd place design logo on the back? Maybe all black with that? Not sure. Also, I'm cool with it being on metal, plastic, glass? or whatever for the business card. Maybe shaped like a shark? Let me know what else you need? Would like designs in the next day or so. Thank you.
Target Market(s)
Anyone that is cool
Contact Information for Business Card
Name: Dorian Fenwick
Phone: 317.594.8126
inventor/creator/entrepreneur/owner
www.theottertyeamug.example
social media links
https://www.facebook.com/theottertyeamug
https://twitter.com/otter_brew
https://www.instagram.com/theottertyeamug/
I'll get the Pinterest one soon
Colors
Designer to choose colors to be used in the design.
Requirements
Must have
- The Otter Tea Mug
- www.theottertyeamug.example
- social media tags?
- My logos and picture/photo of wine glass
Nice to have
- Maybe shaped like a wine glass or shark
- I'll let you decide but my same colors from my website would be nice

```html
<!DOCTYPE html>
<html lang="en">
<head>
<meta charset="utf-8">
<title>Otter Tea Mug — Business Card</title>
<link rel="stylesheet" href="https://fonts.googleapis.com/css2?family=Noto+Serif:wght@400;700&display=swap">
<style>
  :root {
    --stage: #2d2c2d;
    --card-dark: #1f1f1f;
    --card-red: #b03f40;
    --band-red: #c2474b;
    --wave-light: #d9d9da;
    --text-grey: #8c8c8c;
    --text-soft: #a5a5a5;
    --band-text: #e8e8e8;
    --white: #ffffff;
  }
  * { margin: 0; padding: 0; box-sizing: border-box; }
  html, body {
    width: 1200px; height: 1200px; overflow: hidden;
    background: var(--stage);
  }
  .stage { position: relative; width: 1200px; height: 1200px; }
  .card {
    position: absolute; top: 449px;
    width: 531px; height: 302px; overflow: hidden;
  }
  .card--front {
    left: 60px;
    background: var(--card-dark);
    background-image: repeating-linear-gradient(90deg, rgba(255,255,255,0.018) 0 1px, transparent 1px 3px),
                      repeating-linear-gradient(0deg, rgba(255,255,255,0.015) 0 1px, transparent 1px 3px);
    border: 1px solid #3a3a3a;
  }
  .card--back { left: 609px; background: var(--card-red); }

  .brand-name {
    position: absolute; left: 0; width: 400px; text-align: center;
    font-family: "Noto Serif", serif; font-weight: 400;
    font-size: 24px; color: var(--text-grey); top: 66px;
    white-space: nowrap;
  }
  .card--back .brand-name {
    width: 100%; top: 134px; color: var(--white);
  }
  .holder {
    position: absolute; left: 0; width: 400px; text-align: center;
    font-family: "Noto Serif", serif; color: var(--text-grey);
    white-space: nowrap;
  }
  .holder__name { top: 140px; font-size: 21px; }
  .holder__name strong { font-weight: 700; }
  .holder__role { top: 172px; font-size: 10.5px; color: var(--text-soft); }
  .holder__phone { top: 195px; font-size: 13.5px; font-weight: 700; letter-spacing: 3px; }

  .social-band {
    position: absolute; left: 0; top: 248px; width: 400px; height: 12px;
    background: var(--band-red);
    display: flex; align-items: center; justify-content: space-around;
    padding: 0 10px 0 16px;
    font-family: "Noto Serif", serif; font-size: 8px; color: var(--band-text);
  }
  .social-band__item { display: flex; align-items: center; gap: 3px; white-space: nowrap; }
  .social-band__dot { width: 5px; height: 5px; border-radius: 50%; background: var(--band-text); }
  .website {
    position: absolute; left: 0; width: 400px; top: 269px; text-align: center;
    font-family: "Noto Serif", serif; font-weight: 700; font-size: 9px;
    letter-spacing: 2.4px; color: var(--text-grey); white-space: nowrap;
  }
  .wave { position: absolute; left: 0; top: 0; }
</style>
</head>
<body>
<main class="stage">
  <section class="card card--front" aria-label="Business card front">
    <svg class="wave" width="531" height="302" viewBox="0 0 531 302">
      <defs>
        <linearGradient id="wine" x1="0" y1="0" x2="1" y2="1">
          <stop offset="0" stop-color="#c9464b"/>
          <stop offset="0.5" stop-color="#b7434f"/>
          <stop offset="1" stop-color="#c24548"/>
        </linearGradient>
      </defs>
      <path d="M470 0 C400 30 370 110 375 170 C380 230 400 280 412 302 L531 302 L531 0 Z" fill="var(--wave-light)"/>
      <path role="img" aria-label="Red wine with bubbles and tea leaves inside the curved glass shape" d="M500 0 C420 40 385 110 389 170 C393 225 410 275 422 302 L531 302 L531 0 Z" fill="url(#wine)"/>
    </svg>
    <p class="brand-name">Otter Tea Mug</p>
    <p class="holder holder__name"><strong>Dorian</strong> Fenwick</p>
    <p class="holder holder__role">inventor | creator | entrepreneur | owner</p>
    <p class="holder holder__phone">317.594.8126</p>
    <div class="social-band">
      <span class="social-band__item"><span class="social-band__dot"></span>theottertyeamug</span>
      <span class="social-band__item"><span class="social-band__dot"></span>otter_brew</span>
      <span class="social-band__item"><span class="social-band__dot"></span>theottertyeamug</span>
      <span class="social-band__item"><span class="social-band__dot"></span>theottertyeamug</span>
    </div>
    <p class="website">www.theottertyeamug.example</p>
  </section>

  <section class="card card--back" aria-label="Business card back">
    <p class="brand-name">Otter Tea Mug</p>
  </section>
</main>
</body>
</html>
```